Business card for massage therapy company called Brook Fern Wellness

Need business card for massage therapy company called Brook Fern Wellness. Would like my logo on the front and the back of the card I have 3 options of logos and you can play with what looks better.

Would like this information displayed on the back of the card:

Marcus Ellery
Licensed Massage Therapist
321-555-0147
brookfern-example.com
brookfern_rest_

```html
<!DOCTYPE html>
<html lang="en">
<head>
<meta charset="utf-8">
<title>Brook Fern Wellness — Business Card</title>
<link rel="stylesheet" href="https://fonts.googleapis.com/css2?family=Montserrat:wght@300;400&family=Sacramento&display=swap">
<style>
  :root {
    --backdrop: #b9b9b9;
    --sage: #6f7560;
    --card-white: #ffffff;
    --ink-light: #ffffff;
    --leaf-soft: #dfe1d9;
    --leaf-mid: #8d937e;
  }
  * { box-sizing: border-box; margin: 0; padding: 0; }
  html, body { width: 1200px; height: 1015px; overflow: hidden; }
  body {
    background: var(--backdrop);
    font-family: "Montserrat", sans-serif;
    position: relative;
  }
  .card {
    position: absolute;
    left: 250px;
    width: 700px;
    height: 400px;
    box-shadow: 0 8px 24px rgba(0,0,0,0.18);
    overflow: hidden;
  }
  .card--front { top: 80px; background: var(--sage); }
  .card--back { top: 535px; background: var(--card-white); }

  .brand-name {
    position: absolute;
    left: 0; right: 0;
    top: 170px;
    text-align: center;
    color: var(--ink-light);
    font-family: "Montserrat", sans-serif;
    font-weight: 300;
    font-size: 40px;
    letter-spacing: 3px;
  }

  .badge-ring {
    position: absolute;
    left: 195px; top: 35px;
    width: 330px; height: 330px;
    border: 3px solid var(--sage);
    border-radius: 50%;
  }
  .badge-fill {
    position: absolute;
    left: 212px; top: 52px;
    width: 296px; height: 296px;
    background: var(--sage);
    border-radius: 50%;
    color: var(--ink-light);
    text-align: center;
    padding-top: 64px;
  }
  .badge-fill .person-name {
    font-family: "Sacramento", cursive;
    font-size: 40px;
    line-height: 1;
    font-weight: 400;
  }
  .badge-fill .person-title {
    font-weight: 300;
    font-size: 15px;
    margin-top: 8px;
    letter-spacing: 0.3px;
  }
  .badge-fill .divider {
    width: 40px;
    height: 1px;
    background: var(--ink-light);
    margin: 12px auto 12px;
  }
  .badge-fill .contact-line {
    font-weight: 300;
    font-size: 15px;
    line-height: 24px;
  }

  .leaf-accent {
    position: absolute;
    border-radius: 50%;
  }
  .leaf-accent--ring {
    left: 534px; top: 62px;
    width: 34px; height: 96px;
    background: linear-gradient(160deg, var(--leaf-mid), var(--sage));
    border-radius: 60% 40% 60% 40%;
  }
  .leaf-accent--top {
    left: 630px; top: 30px;
    width: 45px; height: 55px;
    background: var(--leaf-soft);
  }
  .leaf-accent--bottom {
    left: 25px; top: 330px;
    width: 70px; height: 45px;
    background: var(--leaf-soft);
  }
</style>
</head>
<body>
  <section class="card card--front">
    <h1 class="brand-name">Brook Fern Wellness</h1>
  </section>

  <section class="card card--back">
    <div class="leaf-accent leaf-accent--top" role="img" aria-label="Faint sprig of leaves in the top corner"></div>
    <div class="leaf-accent leaf-accent--bottom" role="img" aria-label="Faint sprig of leaves in the bottom corner"></div>
    <div class="badge-ring"></div>
    <div class="badge-fill">
      <p class="person-name">Marcus Ellery</p>
      <p class="person-title">Licensed Massage Therapist</p>
      <div class="divider"></div>
      <p class="contact-line">321-555-0147</p>
      <p class="contact-line">brookfern-example.com</p>
      <p class="contact-line">brookfern_rest_</p>
    </div>
    <div class="leaf-accent leaf-accent--ring" role="img" aria-label="Sprig of sage leaves beside the circle edge"></div>
  </section>
</body>
</html>
```